Media & Printing Company 6 Page Brochure with a Bright Lantern Theme

We are a printing company that offers most media communication services such as design, web design, mobile app and of course printing. All the profits of the company are used to fund a Bright Lantern Organisation called “Bright Lantern”. We are looking for a 6 page brochure, flat size 630mm x 210mm fold down to 210mm x 210mm. The brochure needs to push the need for companies to use our service on a “Corporate Social Responsibility” basis with losing the site that we are printers and designers.

Looking for a clean design with impact. A file is attached which shows our logo and some copy to give you an idea of what we are.

Industry/Entity Type

Communication

```html
<!DOCTYPE html>
<html lang="en">
<head>
<meta charset="utf-8">
<title>Northfold Media Communications – Brochure</title>
<link rel="stylesheet" href="https://fonts.googleapis.com/css2?family=Open+Sans:wght@300;400;600&display=swap">
<style>
  :root{
    --cyan:#27b2e6;
    --magenta:#e0218a;
    --yellow:#f4e61a;
    --band:#e6e8ea;
    --band-dark:#d6d9dc;
    --white:#ffffff;
    --ink:#2b2b2b;
    --ink-soft:#555a5e;
    --brand-blue:#1e8fd0;
    --stage:#e9eaeb;
  }
  *{box-sizing:border-box;margin:0;padding:0}
  html,body{width:1200px;height:800px;overflow:hidden}
  body{
    background:var(--stage);
    font-family:"Open Sans",Arial,sans-serif;
    color:var(--ink);
    position:relative;
  }
  .spread{position:absolute;left:30px;top:30px;width:1140px;height:380px;display:flex;box-shadow:0 4px 14px rgba(0,0,0,.12)}
  .panel{position:relative;width:380px;height:380px;overflow:hidden}
  .body-copy{font-size:8px;line-height:11px;font-weight:400}

  /* panel one: who are we */
  .panel--about{background:var(--cyan);color:var(--white)}
  .about-title{position:absolute;left:26px;top:150px;font-size:25px;font-weight:300;color:var(--white)}
  .about-copy{position:absolute;left:176px;top:34px;width:180px}
  .person-art{position:absolute;left:238px;top:232px;width:34px;height:62px;background:linear-gradient(#2a3a4a,#1c6fa3);border-radius:16px 16px 4px 4px}
  .clients-band{position:absolute;left:0;top:300px;width:380px;height:80px;background:var(--band);color:var(--ink-soft)}
  .clients-tag{position:absolute;left:220px;top:-14px;height:24px;padding:0 12px 0 22px;background:var(--band-dark);color:var(--ink-soft);font-size:13px;font-weight:300;line-height:24px;clip-path:polygon(12px 0,100% 0,100% 100%,12px 100%,0 50%)}
  .clients-copy{position:absolute;left:22px;top:20px;width:330px}

  /* panel two: services */
  .panel--services{background:var(--white)}
  .service{position:absolute;left:0;width:380px}
  .service--web{top:0;height:95px;background:var(--white)}
  .service--design{top:95px;height:90px;background:var(--band)}
  .service--print{top:185px;height:100px;background:var(--white)}
  .service--digital{top:285px;height:95px;background:var(--magenta);color:var(--white)}
  .service-label{position:absolute;font-size:12px;font-weight:400}
  .service-art{position:absolute;border-radius:4px}
  .service--web .service-art{left:14px;top:10px;width:66px;height:68px;background:linear-gradient(135deg,#2fb3e6,#e0218a 55%,#f4e61a)}
  .service--web .service-label{left:82px;top:62px}
  .service--web .body-copy{position:absolute;left:112px;top:12px;width:250px}
  .service--design .body-copy{position:absolute;left:16px;top:12px;width:250px}
  .service--design .service-art{left:290px;top:10px;width:74px;height:60px;background:linear-gradient(135deg,#f08a2c,#f6c08a)}
  .service--design .service-label{left:262px;top:56px}
  .service--print .service-art{left:14px;top:12px;width:80px;height:80px;background:linear-gradient(135deg,#2fb3e6,#e0218a 50%,#f4e61a 75%,#222)}
  .service--print .service-label{left:70px;top:22px}
  .service--print .body-copy{position:absolute;left:110px;top:12px;width:255px}
  .service--digital .body-copy{position:absolute;left:16px;top:12px;width:230px}
  .service--digital .service-art{left:260px;top:12px;width:96px;height:70px;background:linear-gradient(135deg,#f3e6c8,#7fcde0)}
  .service--digital .service-label{left:264px;top:58px;color:var(--white)}

  /* panel three: sustainability */
  .panel--sustain{background:var(--yellow)}
  .butterfly-art{position:absolute;left:36px;top:18px;width:74px;height:64px;background:linear-gradient(#3a3a3a,#8a8a8a);border-radius:40% 40% 30% 30%}
  .sustain-title{position:absolute;left:116px;top:44px;font-size:20px;font-weight:300;color:var(--ink-soft)}
  .fingerprint-art{position:absolute;left:28px;top:102px;width:112px;height:140px;border-radius:50% 50% 46% 46%;background:radial-gradient(circle at 50% 55%,#2b2b2b,#e0218a 45%,#27b2e6 75%,rgba(244,230,26,0) 100%)}
  .talk-label{position:absolute;left:40px;top:252px;font-size:11px;font-weight:400;color:var(--ink-soft)}
  .sustain-copy{position:absolute;left:152px;top:104px;width:210px}
  .digital-band{position:absolute;left:0;top:300px;width:380px;height:80px;background:var(--band);color:var(--ink-soft)}
  .digital-title{position:absolute;left:18px;top:10px;font-size:9px;font-weight:600}
  .digital-copy{position:absolute;left:18px;top:26px;width:340px}

  /* cover */
  .cover{position:absolute;left:440px;top:440px;width:320px;height:320px;background:var(--white);box-shadow:0 4px 14px rgba(0,0,0,.12)}
  .cover-art{position:absolute;left:104px;top:34px;width:112px;height:112px;border-radius:50%;background:radial-gradient(circle,#2b2b2b,#e0218a 40%,#27b2e6 70%,rgba(255,255,255,0) 100%)}
  .cover-tagline{position:absolute;left:0;top:170px;width:320px;text-align:center;font-size:7px;letter-spacing:3px;color:var(--ink-soft)}
  .brand-name{position:absolute;left:0;top:196px;width:320px;text-align:center;font-size:34px;font-weight:600;letter-spacing:1px;color:var(--brand-blue)}
  .brand-sub{position:absolute;left:0;top:242px;width:320px;text-align:center;font-size:8px;letter-spacing:2px;color:var(--brand-blue)}
</style>
</head>
<body>
  <section class="spread">
    <article class="panel panel--about">
      <h2 class="about-title">Who are we?</h2>
      <p class="about-copy body-copy">Northfold Media Communications is a design and print studio that puts every profit to work. Each job we take funds Bright Lantern, a social justice organisation helping people find fair access to housing, education and legal support. When you choose us for your brochures, websites and campaigns, your budget becomes part of a wider commitment to your community. It is corporate social responsibility built into everyday work, with no compromise on quality or care.</p>
      <div class="person-art" role="img" aria-label="Silhouette illustration of a client figure"></div>
      <div class="clients-band">
        <span class="clients-tag">Our Clients</span>
        <p class="clients-copy body-copy">We have the privilege of working with some of the most diverse organisations in the region. Whatever the size or nature of your project, we are here to help you reach people and make a lasting difference.</p>
      </div>
    </article>

    <article class="panel panel--services">
      <div class="service service--web">
        <div class="service-art" role="img" aria-label="Illustration of a figure releasing colourful butterflies"></div>
        <span class="service-label">Web</span>
        <p class="body-copy">Your website is your virtual office, so we make sure it tells your story clearly. We build sites that look sharp on every screen and are simple to keep up to date. We know how to build great websites.</p>
      </div>
      <div class="service service--design">
        <p class="body-copy">From cutting edge graphic design to complete company branding, our team creates clear, bold work that helps your business stand out and speak with one voice across every format.</p>
        <div class="service-art" role="img" aria-label="Illustration of a pencil drawing orange butterflies"></div>
        <span class="service-label">Design</span>
      </div>
      <div class="service service--print">
        <div class="service-art" role="img" aria-label="Illustration of colour ink ribbons with butterflies"></div>
        <span class="service-label">Print</span>
        <p class="body-copy">We offer full colour offset printing for every job, large or small. Our presses deliver consistent, vivid results on a wide range of stocks, with careful finishing and reliable turnaround.</p>
      </div>
      <div class="service service--digital">
        <p class="body-copy">Digital print is ideal for short runs and fast deadlines. Print only what you need, personalise every copy and avoid storing large quantities of stock.</p>
        <div class="service-art" role="img" aria-label="Illustration of pale and blue butterflies"></div>
        <span class="service-label">Digital Print</span>
      </div>
    </article>

    <article class="panel panel--sustain">
      <div class="butterfly-art" role="img" aria-label="Dark butterfly silhouette illustration"></div>
      <h2 class="sustain-title">Sustainability....</h2>
      <div class="fingerprint-art" role="img" aria-label="Multicoloured fingerprint illustration"></div>
      <span class="talk-label">Lets talk printing</span>
      <p class="sustain-copy body-copy">We source our stock from responsible paper suppliers. All our papers come from certified, well managed forests, and our inks are vegetable based wherever possible. We recycle offcuts, reduce waste at every stage and offset the energy our presses use. Choosing us means your printed material supports people and the planet at the same time.</p>
      <div class="digital-band">
        <h3 class="digital-title">Is digital technology alien to you?</h3>
        <p class="digital-copy body-copy">Northfold Media Communications specialises in professional and effective email marketing. We plan, design and send campaigns that reach the right audience, then report clearly on the results so you can see what works.</p>
      </div>
    </article>
  </section>

  <section class="cover">
    <div class="cover-art" role="img" aria-label="Multicoloured fingerprint illustration"></div>
    <p class="cover-tagline">CREATING SOCIAL IMPACT</p>
    <p class="brand-name">NORTHFOLD</p>
    <p class="brand-sub">MEDIA COMMUNICATIONS</p>
  </section>
</body>
</html>
```